Design a double sided creative business card

Design is for a adult toy company. Client wants it to be colorful and creative.
Attached are two company logos, please advise if you need a better image.

7TEAMGLOW
Rhona T
Consultant
7GlowwithRhonaT@mailbox-example.net
482-905-1378
Friendspace @7glowwithRhonaT

See what the GLOW is about!

```html
<!DOCTYPE html>
<html lang="en">
<head>
<meta charset="utf-8">
<title>7TEAMGLOW – Business Card</title>
<link rel="stylesheet" href="https://fonts.googleapis.com/css2?family=Open+Sans:wght@400;600;800&display=swap">
<style>
  :root {
    --page-bg: #e9e7e4;
    --card-dark: #2b2b2b;
    --card-darker: #1c1c1c;
    --magenta: #c2198f;
    --white: #ffffff;
    --soft-white: #ececec;
    --muted: #b9b9b9;
  }
  * { box-sizing: border-box; margin: 0; padding: 0; }
  html, body {
    width: 1200px; height: 800px; overflow: hidden;
    background: var(--page-bg);
    font-family: "Open Sans", sans-serif;
  }
  .stage {
    width: 1200px; height: 800px;
    display: flex; align-items: center; justify-content: center; gap: 60px;
  }
  .card {
    position: relative;
    width: 520px; height: 297px;
    background: linear-gradient(135deg, var(--card-dark), var(--card-darker));
    overflow: hidden;
    box-shadow: 0 10px 28px rgba(0,0,0,0.25);
  }
  .card-bands { position: absolute; left: 0; bottom: 0; width: 520px; height: 297px; }

  /* Front */
  .front-logo {
    position: absolute; top: 78px; left: 0; right: 0;
    display: flex; align-items: center; justify-content: center; gap: 14px;
  }
  .front-logo .mark-square { width: 26px; height: 26px; background: var(--magenta); }
  .front-logo .brand-name {
    color: var(--soft-white); font-weight: 800; font-size: 62px; letter-spacing: 1px;
  }

  /* Back */
  .name-block { position: absolute; top: 44px; left: 0; display: flex; align-items: center; }
  .name-block .accent-square { width: 24px; height: 22px; background: var(--magenta); margin-right: 14px; }
  .name-block .person-name {
    color: var(--white); font-weight: 600; font-size: 15px; letter-spacing: 4px; line-height: 1;
  }
  .name-block .person-role {
    color: var(--muted); font-size: 9px; letter-spacing: 2px; margin-top: 3px;
  }
  .back-logo {
    position: absolute; top: 52px; right: 26px;
    color: var(--soft-white); font-weight: 800; font-size: 30px; letter-spacing: 0.5px;
  }
  .rule {
    position: absolute; top: 102px; left: 38px; width: 250px; height: 3px; background: var(--magenta);
  }
  .contacts { position: absolute; top: 122px; left: 38px; list-style: none; }
  .contacts li {
    display: flex; align-items: center; gap: 10px;
    color: var(--soft-white); font-size: 11px; margin-bottom: 9px;
  }
  .contacts .icon {
    width: 18px; height: 18px; border-radius: 50%; background: var(--magenta);
    display: flex; align-items: center; justify-content: center; flex: none;
  }
</style>
</head>
<body>
<main class="stage">

  <section class="card card-back" aria-label="Card back with contact details">
    <div class="name-block">
      <span class="accent-square"></span>
      <div>
        <p class="person-name">RHONA T</p>
        <p class="person-role">CONSULTANT</p>
      </div>
    </div>
    <p class="back-logo">7TEAMGLOW</p>
    <div class="rule"></div>
    <ul class="contacts">
      <li>
        <span class="icon">
          <svg width="10" height="10" viewBox="0 0 24 24"><path fill="#fff" d="M6.6 10.8a15 15 0 0 0 6.6 6.6l2.2-2.2c.3-.3.7-.4 1-.2 1.1.4 2.3.6 3.6.6.6 0 1 .4 1 1V20c0 .6-.4 1-1 1A17 17 0 0 1 3 4c0-.6.4-1 1-1h3.5c.6 0 1 .4 1 1 0 1.3.2 2.5.6 3.6.1.3 0 .7-.2 1z"/></svg>
        </span>
        482-905-1378
      </li>
      <li>
        <span class="icon">
          <svg width="8" height="8" viewBox="0 0 10 10"><circle cx="5" cy="5" r="4" fill="#fff"/></svg>
        </span>
        Friendspace @7glowwithRhonaT
      </li>
      <li>
        <span class="icon">
          <svg width="10" height="8" viewBox="0 0 20 14"><rect x="1" y="1" width="18" height="12" fill="none" stroke="#fff" stroke-width="2"/><path d="M1 1l9 7 9-7" fill="none" stroke="#fff" stroke-width="2"/></svg>
        </span>
        7GlowwithRhonaT@mailbox-example.net
      </li>
    </ul>
    <svg class="card-bands" viewBox="0 0 520 297" aria-hidden="true">
      <polygon points="0,246 268,246 262,262 0,262" fill="var(--white)"/>
      <polygon points="276,246 414,238 408,254 270,262" fill="var(--magenta)"/>
      <polygon points="422,238 520,232 520,248 416,254" fill="var(--white)"/>
      <polygon points="0,268 520,262 520,266 0,272" fill="#3a3a3a"/>
    </svg>
  </section>

  <section class="card card-front" aria-label="Card front with brand name">
    <div class="front-logo">
      <span class="mark-square"></span>
      <span class="brand-name">7TEAMGLOW</span>
    </div>
    <svg class="card-bands" viewBox="0 0 520 297" aria-hidden="true">
      <polygon points="0,222 232,236 226,256 0,242" fill="var(--white)"/>
      <polygon points="240,237 360,244 354,272 234,265" fill="var(--magenta)"/>
      <polygon points="368,245 520,254 520,274 362,265" fill="var(--white)"/>
    </svg>
  </section>

</main>
</body>
</html>
```